GDFH Business Card

Looking for a business card design to incorporate our branding. We want to only use the colors listing in the Branding Package (attached).
Updates

Target Market(s)

People who need their phone or device fixed.

Industry/Entity Type

Electronics

Contact Information for Business Card

Please use:

Gadget Fix Haven LLC
4870 S Ridgecrest Pkwy
Suite 318
San Antonio, TX 78291

Wendell Thorsby, Store Manager

(210) 555-0147

Requirements
Must have
• Must include the colors that are contained within the Branding Package PDF file.

```html
<!DOCTYPE html>
<html lang="en">
<head>
<meta charset="utf-8">
<title>Gadget Fix Haven Business Card</title>
<link href="https://fonts.googleapis.com/css2?family=Open+Sans:wght@400;600;700&display=swap" rel="stylesheet">
<style>
  :root {
    --backdrop: #e9e6e1;
    --card-white: #ffffff;
    --card-dark: #2b2b2c;
    --brand-orange: #f25a0c;
    --brand-lime: #cfd957;
    --ink: #2a2a2a;
    --logo-light: #ffffff;
  }
  html, body {
    margin: 0;
    width: 1200px;
    height: 900px;
    overflow: hidden;
    background: var(--backdrop);
    font-family: "Open Sans", Arial, sans-serif;
  }
  .canvas {
    position: relative;
    width: 1200px;
    height: 900px;
  }
  .card {
    position: absolute;
    width: 630px;
    height: 360px;
    left: 285px;
    box-shadow: 0 6px 18px rgba(0,0,0,0.18);
    overflow: hidden;
  }
  .card-back { top: 70px; background: var(--card-dark); }
  .card-front { top: 470px; background: var(--card-white); }

  .brand-mark {
    position: absolute;
    display: flex;
    align-items: center;
    gap: 16px;
    font-weight: 400;
    white-space: nowrap;
  }
  .brand-mark .mark-square {
    width: 46px;
    height: 46px;
    border-radius: 9px;
    flex: none;
  }
  .card-back .brand-mark {
    left: 120px; top: 152px;
    font-size: 40px;
    color: var(--logo-light);
  }
  .card-back .mark-square { border: 3px solid var(--logo-light); box-sizing: border-box; }

  .card-front .brand-mark {
    left: 300px; top: 160px;
    font-size: 30px;
    color: var(--brand-orange);
  }
  .card-front .mark-square { width: 38px; height: 38px; background: var(--brand-orange); border-radius: 7px; }

  .decor { position: absolute; inset: 0; }

  .person { position: absolute; left: 60px; top: 20px; }
  .person-name { margin: 0; font-size: 18px; font-weight: 700; color: var(--brand-orange); line-height: 1.2; }
  .person-title { margin: 0; font-size: 11px; color: var(--ink); }

  .phone {
    position: absolute; left: 36px; top: 122px;
    display: flex; align-items: center; gap: 9px;
    font-size: 14px; color: var(--ink);
  }
  .phone svg { width: 11px; height: 11px; }

  .company { position: absolute; left: 36px; top: 168px; }
  .company-name { margin: 0 0 2px; font-size: 13px; font-weight: 700; color: var(--brand-orange); }
  .company-address { margin: 0; font-style: normal; font-size: 13.5px; color: var(--ink); line-height: 1.35; }
</style>
</head>
<body>
<main class="canvas">

  <section class="card card-back" aria-label="Business card back">
    <div class="brand-mark">
      <span class="mark-square"></span>
      <span class="brand-name">Gadget Fix Haven</span>
    </div>
  </section>

  <section class="card card-front" aria-label="Business card front">
    <svg class="decor" viewBox="0 0 630 360" width="630" height="360" aria-hidden="true">
      <polygon points="0,0 32,0 0,30" fill="var(--brand-lime)"/>
      <polygon points="14,48 40,22 52,22 52,48" fill="var(--brand-orange)"/>
      <polygon points="0,244 236,244 212,276 0,276" fill="var(--brand-lime)"/>
      <polygon points="220,290 630,290 630,340 0,340 0,330 196,330" fill="var(--brand-orange)"/>
      <polygon points="0,276 212,276 196,330 0,330" fill="var(--card-white)"/>
      <rect x="0" y="340" width="630" height="20" fill="var(--card-white)"/>
    </svg>

    <header class="person">
      <h1 class="person-name">Wendell Thorsby</h1>
      <p class="person-title">Store Manager</p>
    </header>

    <div class="phone">
      <svg viewBox="0 0 24 24" aria-hidden="true"><path fill="var(--brand-orange)" d="M6.6 10.8a15.1 15.1 0 0 0 6.6 6.6l2.2-2.2a1 1 0 0 1 1-.25 11.4 11.4 0 0 0 3.6.57 1 1 0 0 1 1 1V20a1 1 0 0 1-1 1A17 17 0 0 1 3 4a1 1 0 0 1 1-1h3.5a1 1 0 0 1 1 1c0 1.25.2 2.45.57 3.6a1 1 0 0 1-.25 1z"/></svg>
      <span>(210) 555-0147</span>
    </div>

    <div class="company">
      <p class="company-name">Gadget Fix Haven LLC</p>
      <address class="company-address">4870 S Ridgecrest Pkwy Suite<br>318 San Antonio, TX 78291</address>
    </div>

    <div class="brand-mark">
      <span class="mark-square"></span>
      <span class="brand-name">Gadget Fix Haven</span>
    </div>
  </section>

</main>
</body>
</html>
```